Postcard Design

TobysKit connects Golf Pro Shops to consumers and in doing so drives new business to the Golf Course through online sales of Pro Shop Merchandise.

Currently, most Golf Pro Shops don't have an online presence for their retail merchandise (golf balls, shirts, clubs, shoes, etc.). Typically a significant amount of their merchandise is sold at a discounted rate after sitting on the racks for a period of time. We will work with pro-shops to get their surplus merchandise online and sold to local golfers...our catch however is that the course does not ship the merchandise, but rather the purchase goes to the course to pick it up and hopefully book a time to play. We like to market three simple steps: 1)Buy your Gear, 2)Pick up your Gear, 3)Play golf

This postcard is one we want to send to the golf pro-shops to encourage them to sign up for our service. This is what we tell the pro-shop managers:

First – you decide what you want to put online
Second – upload merchandise details to your online store at TobysKit.com
Third – Get paid (automatically) and fill tee times
Obviously it’s a bit more involved than that, but not much. TobysKit has brought the local pro-shop to the online consumer. And with no shipping, the only thing you and your staff will need to do is put aside the sold merchandise until the customer comes to pick it up…and hopefully by now they have also booked a round of golf to play while there. This is an opportunity to not only move the merchandise on your shelves; it’s an opportunity to introduce new golfers to your course…golfers who will return time and again, hopefully with three (or more) of their buddies. TobysKit – Buy Near Your Tee

Also, there is no cost to the pro-shop unless something is sold, then at time of payment thru CoinLane, the transaction is split with x% going to the pro-shop and x% going to TobysKit.

Contact info to include on card:
Instead of "Contact Info" though, maybe something like "Talk to Toby", followed by the info...again, this should feel somewhat casual and personal.

www.tobyskit-demo.com
855-TOBYSKITS (855-862-9754)
info@tobyskit-demo.com

I've uploaded our logo files...sorry, thought I had done that in the original submission. FYI - I want something simple...just something to get the Pro-shop Manager to look at the card and take action/go to our website or send an email.

Target Market(s)

This is meant to go to Golf Pro-Shop merchandising managers

Industry/Entity Type

Business

Font styles to use
Other font styles liked:
• Insignia

Requirements
Must have
• Simple
This should feel like it's coming from Toby himself...more of a personal card.
Should not have
• Not too much emphasis on "golf"...they work at golf-shops, they know what a course looks like! :)

```html
<!DOCTYPE html>
<html lang="en">
<head>
<meta charset="utf-8">
<title>TobysKit Postcard</title>
<link rel="stylesheet" href="https://fonts.googleapis.com/css2?family=Questrial&display=swap">
<style>
  :root {
    --bg: #e4e4e4;
    --card: #ffffff;
    --ink: #1a1a1a;
    --accent: #d9541e;
    --muted: #8f8f8f;
    --rule: #cfcfcf;
    --photo-light: #f6f6f6;
    --photo-mid: #dcdcdc;
  }
  * { box-sizing: border-box; margin: 0; padding: 0; }
  html, body {
    width: 1200px; height: 1200px; overflow: hidden;
    background: var(--bg);
    font-family: "Questrial", sans-serif;
  }
  .postcard {
    position: absolute; left: 50px; top: 212px;
    width: 1100px; height: 777px;
    background: var(--card);
    box-shadow: 0 2px 10px rgba(0,0,0,0.12);
  }
  .brand { position: absolute; left: 94px; top: 57px; display: flex; align-items: center; }
  .brand-dot {
    width: 82px; height: 82px; border-radius: 50%;
    background: var(--muted);
  }
  .brand-text { margin-left: 28px; }
  .brand-name {
    font-size: 26px; letter-spacing: 9px; color: var(--muted); line-height: 1;
  }
  .brand-tagline {
    font-size: 11px; letter-spacing: 2px; color: var(--muted);
    margin-top: 10px; margin-left: 114px;
  }
  .steps { position: absolute; left: 103px; top: 195px; list-style: none; }
  .step { display: flex; align-items: flex-start; margin-bottom: 18px; }
  .step-num {
    flex: none; width: 46px; height: 46px; border-radius: 50%;
    border: 2px solid #c4c4c4; color: var(--accent);
    display: flex; align-items: center; justify-content: center;
    font-size: 30px; margin-top: 2px;
  }
  .step-text {
    margin-left: 18px; font-size: 19px; line-height: 27px;
    color: var(--accent); letter-spacing: 0.6px;
  }
  .step-text b { font-weight: 400; color: var(--ink); }
  .hero-photo { position: absolute; left: 230px; top: 0; width: 480px; height: 640px; }
  .stamp-box {
    position: absolute; left: 905px; top: 59px; width: 123px; height: 143px;
    border: 2px solid #bdbdbd;
  }
  .address-lines { position: absolute; left: 659px; top: 274px; width: 369px; }
  .address-line { height: 70.5px; border-top: 1.5px solid var(--rule); }
  .talk {
    position: absolute; left: 102px; top: 643px;
    font-size: 27px; color: var(--accent);
  }
  .contact {
    position: absolute; left: 102px; top: 693px;
    font-size: 19px; color: var(--ink); letter-spacing: 0.3px;
  }
</style>
</head>
<body>
  <main class="postcard">
    <div class="brand">
      <div class="brand-dot"></div>
      <div class="brand-text">
        <div class="brand-name">Tobys Kit</div>
        <div class="brand-tagline">Buy Near Your Tee...</div>
      </div>
    </div>

    <svg class="hero-photo" viewBox="0 0 480 640" role="img" aria-label="Photo of a golf iron about to strike a golf ball resting on a white tee">
      <defs>
        <radialGradient id="photoGlow" cx="55%" cy="55%" r="55%">
          <stop offset="0%" stop-color="#e2e2e2"/>
          <stop offset="100%" stop-color="#ffffff" stop-opacity="0"/>
        </radialGradient>
      </defs>
      <rect width="480" height="640" fill="url(#photoGlow)"/>
    </svg>

    <ol class="steps">
      <li class="step"><span class="step-num">1</span>
        <p class="step-text"><b>you decide</b> what you want<br>to put online</p></li>
      <li class="step"><span class="step-num">2</span>
        <p class="step-text"><b>upload merchandise</b> details<br>to your online store at<br>TobysKit.com</p></li>
      <li class="step"><span class="step-num">3</span>
        <p class="step-text"><b>get paid</b> (automatically)<br>and fill tee times</p></li>
    </ol>

    <div class="stamp-box"></div>
    <div class="address-lines">
      <div class="address-line"></div>
      <div class="address-line"></div>
      <div class="address-line"></div>
      <div class="address-line"></div>
      <div class="address-line"></div>
    </div>

    <p class="talk">Talk to Toby!</p>
    <p class="contact">toby@tobyskit-demo.com &bull; www.tobyskit-demo.com &bull; 855-TOBYSKITS (855-862-9754)</p>
  </main>
</body>
</html>
```